Classic Minimalistic Business Card

Design a classic, minimalistic Business Card. Please find inspiration in the attached Classic Minimalistic examples. My information:
Name: Glen Ovamir
Company: Ovamir Capital
Logo: OC
Address: 1470 N Thornwick Rd, Suite 210 | Lorwick, IL 60177
Phone: 630-555-0192
Email: glenovamir@pvt.insure
Slogan: Building Strength Through Capital

Feel free to leave out any of the information above except my name.

I have selected Double-sided, but I am also open to Single-sided

Target Market(s)

22-70. income greater than 150k/year

Industry/Entity Type

Finance

Contact Information for Business Card

See Project Description

Requirements
Must have
• Ivory or "antiqued" background similar to the reference pictures

```html
<!DOCTYPE html>
<html lang="en">
<head>
<meta charset="utf-8">
<title>Glen Ovamir — Business Card</title>
<link rel="stylesheet" href="https://fonts.googleapis.com/css2?family=Pinyon+Script&family=Questrial&family=Cormorant+Garamond:wght@500&family=EB+Garamond:ital@1&display=swap">
<style>
  :root {
    --backdrop: #a8aaac;
    --card-ivory: #ede7da;
    --card-ivory-light: #f2ede2;
    --card-ivory-shade: #e3dccc;
    --ink: #1d1c1b;
    --ink-script: #2a2826;
  }
  * { margin: 0; padding: 0; box-sizing: border-box; }
  html, body {
    width: 1200px;
    height: 1183px;
    overflow: hidden;
    background: var(--backdrop);
  }
  .canvas {
    position: relative;
    width: 1200px;
    height: 1183px;
  }
  .card {
    position: absolute;
    left: 290px;
    width: 610px;
    height: 370px;
    background: radial-gradient(ellipse at 45% 35%, var(--card-ivory-light) 0%, var(--card-ivory) 55%, var(--card-ivory-shade) 100%);
    color: var(--ink);
    text-align: center;
  }
  .card--front { top: 121px; }
  .card--back { top: 713px; }

  .card__line {
    position: absolute;
    left: 0;
    right: 0;
    font-weight: normal;
  }
  .phone {
    top: 45px;
    font-family: "Questrial", sans-serif;
    font-size: 15px;
    letter-spacing: 0.06em;
  }
  .name {
    top: 136px;
    font-family: "Pinyon Script", cursive;
    font-size: 80px;
    line-height: 1.2;
    color: var(--ink-script);
  }
  .email {
    top: 310px;
    font-family: "Questrial", sans-serif;
    font-size: 14px;
    letter-spacing: 0.14em;
    text-transform: uppercase;
  }
  .address {
    top: 39px;
    font-family: "Questrial", sans-serif;
    font-size: 16px;
    line-height: 23px;
    font-variant: small-caps;
    letter-spacing: 0.05em;
  }
  .company {
    top: 166px;
    font-family: "Cormorant Garamond", serif;
    font-weight: 500;
    font-size: 30px;
    letter-spacing: 0.45em;
    padding-left: 0.45em;
    font-variant: small-caps;
  }
  .slogan {
    top: 267px;
    font-family: "EB Garamond", serif;
    font-style: italic;
    font-size: 17px;
  }
</style>
</head>
<body>
<main class="canvas">
  <section class="card card--front" aria-label="Card front">
    <p class="card__line phone">630-555-0192</p>
    <h1 class="card__line name">Glen Ovamir</h1>
    <p class="card__line email">glenovamir@pvt.insure</p>
  </section>

  <section class="card card--back" aria-label="Card back">
    <p class="card__line address">1470 N Thornwick Rd, Suite 210<br>Lorwick, IL 60177</p>
    <h2 class="card__line company">Ovamir Capital</h2>
    <p class="card__line slogan">Building Strength Through Capital</p>
  </section>
</main>
</body>
</html>
```